Company notecard redesign

We'd like a redesign done of our company notecards. We use these cards to hand-write messages to clients/potential clients. This could be thank-you cards, congratulations cards, check-in cards, etc. Current cards are 5.5" x 8.5" and fold in half (you'll see the fold mark on the scanned image). We would like the new cards to not fold, and just be 5.5" x 4.25". We do like the little dog head you'll see on the inside notecard scan as the dog is our logo. I've also attached our "professional" logo with our new tagline. Address info you see on the outside notecard scan is correct.

Target Market(s)

Brindlequay and CRM clients

Industry/Entity Type

It Company

Colors
3377b5
ffffff
fff8ef

Requirements
Must have
• Our logo, some contact info
Nice to have
• Dog head from our current notecard scan

```html
<!DOCTYPE html>
<html lang="en">
<head>
<meta charset="utf-8">
<title>Keston Notecard — Front and Back</title>
<link rel="stylesheet" href="https://fonts.googleapis.com/css2?family=Roboto:wght@700&family=Roboto+Condensed:wght@400;700&family=Open+Sans:wght@400&display=swap">
<style>
  :root {
    --page: #ffffff;
    --label-grey: #9a9a9a;
    --card-edge: #c9c9c9;
    --sky: #96bbdc;
    --mist: #c0d6ea;
    --brand-blue: #2d78b8;
    --navy: #0f2f4c;
    --emblem-blue: #7fb0d4;
    --tagline-grey: #7a7a7a;
    --faint-emblem: #ecf2f7;
    --faint-name: #bfd0de;
    --soft-blue-text: #8fb4d6;
    --white: #ffffff;
  }
  html, body {
    margin: 0;
    padding: 0;
    width: 1200px;
    height: 1000px;
    overflow: hidden;
    background: var(--page);
  }
  .sheet {
    position: relative;
    width: 1200px;
    height: 1000px;
    font-family: "Roboto Condensed", "Arial Narrow", sans-serif;
  }
  .side-label {
    position: absolute;
    top: 266px;
    margin: 0;
    font-family: "Roboto", Arial, sans-serif;
    font-weight: 700;
    font-size: 16px;
    color: var(--label-grey);
    letter-spacing: 0.2px;
  }
  .side-label--front { left: 17px; }
  .side-label--back { right: 17px; }

  .card {
    position: absolute;
    top: 293px;
    height: 443px;
    box-sizing: border-box;
    overflow: hidden;
  }
  .card--front {
    left: 17px;
    width: 574px;
    border: 1px solid var(--card-edge);
    background: var(--white);
  }
  .card--back {
    left: 610px;
    width: 573px;
    border: 1px solid #8a9aa8;
    background: var(--white);
  }

  /* front */
  .front-emblem {
    position: absolute;
    left: 200px;
    top: 122px;
    width: 175px;
    height: 175px;
    border-radius: 50%;
    background: var(--faint-emblem);
  }
  .contact-line {
    position: absolute;
    left: 0;
    right: 0;
    top: 402px;
    display: flex;
    justify-content: center;
    align-items: baseline;
    gap: 12px;
    font-size: 11px;
    white-space: nowrap;
  }
  .contact-line .phone,
  .contact-line .web { font-weight: 700; }
  .contact-line--front { color: var(--soft-blue-text); }
  .contact-line--front .mini-brand {
    display: flex;
    align-items: center;
    gap: 3px;
    margin-right: 24px;
    font-weight: 700;
    font-size: 17px;
    color: var(--faint-name);
    letter-spacing: 0.5px;
    transform: translateY(3px);
  }
  .mini-brand .dot {
    width: 11px;
    height: 11px;
    border-radius: 50%;
    background: var(--faint-name);
  }
  .contact-line--back { color: var(--white); }

  /* back */
  .band { position: absolute; left: 0; right: 0; }
  .band--sky { top: 0; height: 90px; background: var(--sky); }
  .band--mist { top: 95px; height: 27px; background: var(--mist); }
  .band--brand { top: 240px; bottom: 0; background: var(--brand-blue); }

  .brand-lockup {
    position: absolute;
    left: 0;
    right: 0;
    top: 136px;
    text-align: center;
  }
  .brand-row {
    display: inline-flex;
    align-items: center;
    gap: 8px;
  }
  .brand-name {
    font-family: "Roboto Condensed", "Arial Narrow", sans-serif;
    font-weight: 700;
    font-size: 76px;
    line-height: 62px;
    letter-spacing: 3px;
    color: var(--navy);
  }
  .brand-mark {
    width: 54px;
    height: 54px;
    border-radius: 50%;
    background: var(--emblem-blue);
  }
  .tagline {
    margin: 8px 0 0;
    font-family: "Open Sans", Arial, sans-serif;
    font-size: 13px;
    letter-spacing: 2px;
    color: var(--tagline-grey);
  }
</style>
</head>
<body>
  <main class="sheet">
    <h2 class="side-label side-label--front">FRONT</h2>
    <h2 class="side-label side-label--back">BACK</h2>

    <section class="card card--front" aria-label="Notecard front">
      <div class="front-emblem" role="img" aria-label="Faint company emblem watermark area"></div>
      <div class="contact-line contact-line--front">
        <span class="mini-brand"><span>KESTON</span><span class="dot"></span></span>
        <span class="phone">555-014-2290</span>
        <span class="address">1180 W Orchard Ave. Suite 4, Brookvale, IN 46000</span>
        <span class="web">KESTONTECH.com</span>
      </div>
    </section>

    <section class="card card--back" aria-label="Notecard back">
      <div class="band band--sky"></div>
      <div class="band band--mist"></div>
      <div class="brand-lockup">
        <div class="brand-row">
          <span class="brand-name">KESTON</span>
          <span class="brand-mark"></span>
        </div>
        <p class="tagline">A CLOUD CONSULTING COMPANY</p>
      </div>
      <div class="band band--brand"></div>
      <div class="contact-line contact-line--back">
        <span class="phone">555-014-2290</span>
        <span class="address">1180 W Orchard Ave. Suite 4, Brookvale, IN 46000</span>
        <span class="web">KESTONTECH.com</span>
      </div>
    </section>
  </main>
</body>
</html>
```